Plumber needs a business card

I need a new business card for my plumbing business. I dont have a logo at the moment but I want business cards that are simple but very professional. I want to look like
Name: Mitch Dorley
Address: (just make one up)
Phone: 0455 318 726
Email: mitch@dorleymail.com
Colors to use:
Blacks, blues, silvers

```html
<!DOCTYPE html>
<html lang="en">
<head>
<meta charset="utf-8">
<title>Mitch Dorley – Plumbing Business Card</title>
<link rel="stylesheet" href="https://fonts.googleapis.com/css2?family=Lato:wght@400;700&display=swap">
<style>
  :root {
    --page-bg: #d8d5d1;
    --frost-light: #f1f1f3;
    --frost-mid: #dcdde2;
    --navy: #1f2a78;
    --navy-deep: #141b52;
    --edge-black: #1a1a1e;
    --edge-silver: #b8b3a8;
    --text-light: #e6e7f0;
    --text-soft: #c9cbe0;
    --text-tan: #b8a684;
    --brand-navy: #2a3585;
  }
  * { margin: 0; padding: 0; box-sizing: border-box; }
  html, body {
    width: 1200px;
    height: 970px;
    overflow: hidden;
    background: var(--page-bg);
    font-family: "Lato", sans-serif;
  }
  .business-card {
    position: absolute;
    left: 120px;
    top: 218px;
    width: 960px;
    height: 534px;
    border-radius: 22px;
    box-shadow: 0 10px 30px rgba(0,0,0,0.18);
  }
  .card-shapes {
    position: absolute;
    inset: 0;
  }
  .brand-mark {
    position: absolute;
    left: 258px;
    top: 273px;
    transform: translate(-50%, -50%);
    display: flex;
    align-items: center;
    gap: 14px;
    font-weight: 700;
    font-size: 40px;
    color: var(--brand-navy);
    white-space: nowrap;
  }
  .brand-dot {
    width: 18px;
    height: 18px;
    border-radius: 50%;
    background: var(--brand-navy);
  }
  .card-info {
    position: absolute;
    right: 82px;
    top: 0;
    text-align: right;
  }
  .owner-name {
    position: absolute;
    right: 0;
    top: 106px;
    font-weight: 700;
    font-size: 28px;
    color: var(--text-light);
    white-space: nowrap;
  }
  .owner-role {
    position: absolute;
    right: 0;
    top: 142px;
    font-size: 21px;
    color: var(--text-soft);
    white-space: nowrap;
  }
  .contact-list {
    position: absolute;
    right: -32px;
    top: 262px;
    list-style: none;
  }
  .contact-item {
    display: flex;
    justify-content: flex-end;
    align-items: center;
    gap: 12px;
    height: 26px;
    font-size: 20px;
    color: var(--text-light);
    white-space: nowrap;
  }
  .contact-icon {
    width: 20px;
    height: 20px;
    flex: none;
  }
  .address {
    position: absolute;
    right: 0;
    top: 374px;
    font-size: 20px;
    line-height: 26px;
    color: var(--text-tan);
    white-space: nowrap;
  }
</style>
</head>
<body>
  <div class="business-card">
    <svg class="card-shapes" width="960" height="534" viewBox="0 0 960 534">
      <defs>
        <clipPath id="card-clip">
          <rect width="960" height="534" rx="22"/>
        </clipPath>
        <linearGradient id="frost-grad" x1="0" y1="0" x2="1" y2="1">
          <stop offset="0" stop-color="var(--frost-light)"/>
          <stop offset="1" stop-color="var(--frost-mid)"/>
        </linearGradient>
        <linearGradient id="navy-grad" x1="0" y1="0" x2="1" y2="1">
          <stop offset="0" stop-color="var(--navy)"/>
          <stop offset="1" stop-color="var(--navy-deep)"/>
        </linearGradient>
      </defs>
      <g clip-path="url(#card-clip)">
        <rect class="frost-panel" width="960" height="534" fill="url(#frost-grad)"/>
        <path class="edge-black" d="M462,0 Q652,267 420,534 L960,534 L960,0 Z" fill="var(--edge-black)"/>
        <path class="edge-silver" d="M476,0 Q662,267 438,534" fill="none" stroke="var(--edge-silver)" stroke-width="2"/>
        <path class="navy-panel" d="M480,0 Q665,267 442,534 L960,534 L960,0 Z" fill="url(#navy-grad)"/>
      </g>
      <rect width="959" height="533" x="0.5" y="0.5" rx="22" fill="none" stroke="#c4c4c8" stroke-width="1"/>
    </svg>

    <div class="brand-mark"><span class="brand-dot"></span>Dorley</div>

    <div class="card-info">
      <p class="owner-name">Mitch Dorley</p>
      <p class="owner-role">Plumbing Business</p>

      <ul class="contact-list">
        <li class="contact-item">000.000.0000
          <svg class="contact-icon" viewBox="0 0 20 20"><rect x="6" y="2" width="8" height="16" rx="1.5" fill="none" stroke="var(--text-light)" stroke-width="1.6"/><line x1="9" y1="15" x2="11" y2="15" stroke="var(--text-light)" stroke-width="1.6"/></svg>
        </li>
        <li class="contact-item">0455 318 726
          <svg class="contact-icon" viewBox="0 0 20 20"><path d="M5 3 L8 3 L9 7 L7 8.5 Q9 12 11.5 13 L13 11 L17 12 L17 15 Q16 17 13 16.5 Q6 14 3.5 6 Q3 4 5 3 Z" fill="var(--text-light)"/></svg>
        </li>
        <li class="contact-item">mitch@dorleymail.com
          <svg class="contact-icon" viewBox="0 0 20 20"><rect x="2" y="5" width="16" height="11" fill="var(--text-light)"/><path d="M2 5 L10 11 L18 5" fill="none" stroke="var(--navy)" stroke-width="1.4"/></svg>
        </li>
      </ul>

      <p class="address">Suite 102, Street name,<br>State, Zip 2034, Country</p>
    </div>
  </div>
</body>
</html>
```